The logo name is "Harbon Vellis". The name of the product will be "Tavoren Calm". This product is specifically formulated for amputees. Therefore under the product name it should state "for amputees". The catch phrase will be "Experience Harbon gain Wellstride"
These are the things we need on the label:
Logo, product name, "for amputees", "Experience Harbon gain Wellstride", Safe, Effective, Directions: spray on problem areas, no need to dry off. harbonvellis.example, Made in Canada, 500ml.
The MOST IMPORTANT and therefore the most prominent thing on this lable will be the LOGO! The second most prominent thing will be the word "Calm" We want to keep it very plain, very simple, very unclutered. Keep in mind that this lable will be placed on a white bottle or have a white back ground. The 500ml white PE bottle with trigger sprayer will have a tear drop label. See attached die line (S-294).
We want to stay with the colours that goes with the colour scheme of the logo. See attached logo. Soft colours. We do not want a picture! We would like the lable to be classy and rich.
Updates
The logo name is "Harbon Vellis". The name of the product will be "Tavoren Calm". This product is specificlly formulated for amputees. Therefore under the product name it should state "for amputees". The catch phrase will be "Experience Harbon gain Wellstride"
Logo, product name, "for amputees", catch phrase "Experience Harbon gain Wellstride", Clean, Safe, Effective, Directions: spray on problem areas, no need to dry off. Also Harbon Vellis Corpation, harbonvellis.example, Made in Canada, 500ml.
We want to stay with the colour scheme of the logo. See attached logo. Soft colours. We do not want a picture! We would like the lable to be classy and rich.
This is the offical directive that came from the governing panal of this lable. This panal it not know where it wanted to take this lable that would represent this line until they review all of your submissions, thank you for all your talented hard work. But now it is clear it is time to regroup and hit this objective.
Target Market(s)
Amputees and Parents of.
Industry/Entity Type
Product
Requirements
Must have
- Final product to be in a pdf or an illustrator file

```html
<!DOCTYPE html>
<html lang="en">
<head>
<meta charset="utf-8">
<title>Tavoren Calm – Teardrop Label</title>
<link rel="stylesheet" href="https://fonts.googleapis.com/css2?family=Noto+Serif:ital,wght@0,700;1,700&display=swap">
<style>
  :root {
    --label-teal: #96d0d2;
    --pill-teal: #1fb0b0;
    --sun-yellow: #fbc050;
    --deep-green: #0a5c47;
    --tag-teal: #1fa3a6;
    --paper: #ffffff;
    --glow-tint: #c4e6e6;
  }
  html, body {
    margin: 0;
    padding: 0;
    width: 1155px;
    height: 1200px;
    overflow: hidden;
    background: var(--paper);
  }
  .label-art {
    display: block;
    width: 1155px;
    height: 1200px;
    font-family: "Noto Serif", Georgia, serif;
  }
  .die-line { fill: none; stroke: var(--deep-green); stroke-width: 1.2; }
  .field-teal { fill: var(--label-teal); }
  .band-yellow { fill: var(--sun-yellow); }
  .motif-area { fill: url(#softGlow); }
  .product-name {
    fill: var(--paper);
    font-weight: 700;
    filter: url(#softShadow);
  }
  .audience-pill { fill: var(--pill-teal); }
  .audience-text { fill: var(--paper); font-weight: 700; font-size: 12px; }
  .brand-square { fill: var(--label-teal); }
  .brand-name { fill: var(--deep-green); font-weight: 700; font-size: 32px; }
  .tagline { fill: var(--tag-teal); font-weight: 700; font-style: italic; font-size: 14.5px; }
  .claim-pill { fill: var(--sun-yellow); }
  .claim-text { fill: var(--deep-green); font-weight: 700; font-size: 12px; letter-spacing: .6px; }
  .directions { fill: var(--deep-green); font-weight: 700; font-style: italic; font-size: 9.5px; }
  .maker-info { fill: var(--deep-green); font-weight: 700; font-size: 9.5px; }
</style>
</head>
<body>
<svg class="label-art" viewBox="0 0 940 976" xmlns="http://www.w3.org/2000/svg">
  <defs>
    <clipPath id="teardrop">
      <path id="teardropShape" d="M475 218 C490 212 505 215 515 228 C600 330 700 470 735 620 C750 690 745 760 735 800 C725 840 710 852 690 852 L450 852 C420 852 405 840 398 815 C385 760 383 680 388 590 C400 440 430 300 475 218 Z"/>
    </clipPath>
    <radialGradient id="softGlow" cx="50%" cy="50%" r="50%">
      <stop offset="0" stop-color="#c4e6e6" stop-opacity=".7"/>
      <stop offset="1" stop-color="#c4e6e6" stop-opacity="0"/>
    </radialGradient>
    <filter id="softShadow" x="-10%" y="-20%" width="120%" height="150%">
      <feDropShadow dx="0" dy="1" stdDeviation="2.5" flood-color="#2f5f60" flood-opacity=".55"/>
    </filter>
  </defs>

  <g class="label-body" clip-path="url(#teardrop)">
    <path class="band-yellow" d="M370 200 H760 V508 C700 490 600 482 520 506 C460 526 420 560 370 600 Z"/>
    <path class="field-teal" d="M370 200 H760 V476 C650 470 560 472 490 498 C440 518 405 540 370 565 Z"/>
    <rect class="motif-area" role="img" aria-label="Soft leaf motif" x="425" y="280" width="125" height="85"/>
  </g>

  <use href="#teardropShape" class="die-line"/>

  <text class="product-name" x="427" y="398" font-size="37">Tavoren</text>
  <text class="product-name" x="427" y="438" font-size="37" letter-spacing="1.5">CALM</text>

  <rect class="audience-pill" x="426" y="448" width="173" height="21" rx="10.5"/>
  <text class="audience-text" x="512.5" y="463" text-anchor="middle">Formulated for amputees.</text>

  <rect class="brand-square" x="418" y="608" width="44" height="44"/>
  <text class="brand-name" x="472" y="644">Harbon Vellis</text>

  <text class="tagline" x="578" y="698" text-anchor="middle">Experience Harbon gain Wellstride</text>

  <rect class="claim-pill" x="457" y="739" width="208" height="27" rx="13.5"/>
  <text class="claim-text" x="561" y="757" text-anchor="middle">CLEAN, SAFE &amp; EFFECTIVE.</text>

  <text class="directions" x="466" y="782">Directions: spray on problem areas,</text>
  <text class="directions" x="466" y="795">no need to dry off.</text>

  <text class="maker-info" x="466" y="823">Harbon Vellis Corpation, harbonvellis.example</text>
  <text class="maker-info" x="466" y="838">MADE IN CANADA – 500ml</text>
</svg>
</body>
</html>
```